Promotion for a free HTML weather widget

skyvela (http://www.skyvela.example/) is a meteorological service based in Basel, Switzerland.
We offer a free HTML widget that offers weather forecasts for a selected location anywhere on the world for up to seven days (see http://www.skyvela.example/en_GB/weather/forecast/widgetsetup) which can be included in any other website.
To make the widget more popular and well-known, we would like to add a promotional banner for it on our own homepage. The space where the banner will be located is marked red on the attached banner_location.png.
We have received permissions from three websites that are already using our widget to use a screenshot from their website on this banner.
These websites are:
- http://gazette.norlab.example/ (widget is on the bottom of the page)
- http://www.tonvillage.example/
- http://www.valmira.example/
Requirements
Must have
- - Width: 696px
- Height: 150px to 200px
- fits nicely in our website
- uses screenshots of the three aforementioned websites (widget must be visible, other ads on those website must be unrecognisable)
- Text (English) that praises the most important advantages of the widget: it is free to use, worldwide available, easy to integrate, offers valuable weather information to visitors
- Possibility to change the text on our side for translations

```html
<!DOCTYPE html>
<html lang="en">
<head>
<meta charset="utf-8">
<title>skyvela – Free HTML Widget banner</title>
<link rel="stylesheet" href="https://fonts.googleapis.com/css2?family=Arimo:ital,wght@0,400;0,700;1,700&family=Roboto+Condensed:wght@700&display=swap">
<style>
  :root {
    --blue: #2a9be4;
    --ink: #111111;
    --grey: #6d6d6d;
    --paper: #ffffff;
    --max-orange: #f9a61c;
    --max-amber: #fdc40f;
    --max-yellow: #f7ea1c;
    --min-lime: #a6dc3c;
    --min-green: #52c23a;
    --min-deep: #34b233;
    --icon-sky: #cfe6f8;
    --icon-sun: #f7c842;
    --logo-bg: #111111;
  }
  html, body {
    margin: 0;
    padding: 0;
    width: 1200px;
    height: 345px;
    overflow: hidden;
    background: var(--paper);
  }
  .banner {
    position: relative;
    width: 696px;
    height: 200px;
    transform: scale(1.7241);
    transform-origin: 0 0;
    font-family: "Arimo", Arial, sans-serif;
    color: var(--ink);
  }

  /* Widget preview */
  .widget {
    position: absolute;
    left: 24px;
    top: 4px;
    width: 160px;
  }
  .widget-place {
    font-size: 8px;
    color: var(--grey);
    font-weight: 700;
    margin: 0;
    line-height: 1.2;
  }
  .widget-coords {
    font-size: 6px;
    color: var(--grey);
    margin: 0 0 6px;
  }
  .forecast {
    display: grid;
    grid-template-columns: repeat(5, 28px);
    column-gap: 2px;
    text-align: center;
  }
  .day-name { font-size: 11px; line-height: 12px; }
  .day-date { font-size: 6px; font-weight: 700; line-height: 9px; }
  .day-icon {
    width: 26px;
    height: 24px;
    margin: 1px auto 3px;
    border-radius: 4px;
    background: linear-gradient(160deg, var(--icon-sun) 0 35%, var(--icon-sky) 36%);
  }
  .temp {
    height: 18px;
    line-height: 18px;
    font-size: 11px;
    font-weight: 700;
    margin-bottom: 3px;
  }
  .temp small { font-size: 5px; vertical-align: top; }
  .t-orange { background: var(--max-orange); }
  .t-amber { background: var(--max-amber); }
  .t-yellow { background: var(--max-yellow); }
  .t-lime { background: var(--min-lime); }
  .t-green { background: var(--min-green); }
  .t-deep { background: var(--min-deep); }
  .wind { font-size: 9px; margin-top: 3px; }
  .wind small { font-size: 5px; }

  .brand {
    position: absolute;
    left: 47px;
    top: 150px;
    width: 78px;
    height: 30px;
    border-radius: 5px;
    background: var(--logo-bg);
    color: var(--paper);
    font-size: 15px;
    font-weight: 700;
    line-height: 30px;
    text-align: center;
  }

  /* Promotion copy */
  .pitch {
    position: absolute;
    left: 201px;
    top: 26px;
  }
  .lead {
    margin: 0;
    font-size: 15.5px;
    font-weight: 700;
    letter-spacing: -0.1px;
  }
  .headline {
    margin: 0;
    font-family: "Roboto Condensed", "Arial Narrow", sans-serif;
    font-weight: 700;
    font-size: 50px;
    line-height: 50px;
    color: var(--blue);
    letter-spacing: 0.5px;
  }
  .benefits {
    list-style: none;
    margin: 6px 0 0 4px;
    padding: 0;
    display: grid;
    grid-template-columns: 146px auto;
    row-gap: 5px;
    font-size: 14.5px;
  }
  .benefits li { position: relative; padding-left: 15px; }
  .benefits li::before {
    content: "";
    position: absolute;
    left: 0;
    top: 5px;
    width: 7px;
    height: 7px;
    border-radius: 50%;
    background: var(--blue);
  }
  .cta {
    display: flex;
    align-items: center;
    gap: 6px;
    margin: 14px 0 0 30px;
    font-size: 14.5px;
    font-weight: 700;
    font-style: italic;
    color: var(--blue);
    text-decoration: none;
  }
</style>
</head>
<body>
<div class="banner">
  <section class="widget" aria-label="Weather widget example">
    <p class="widget-place">Météo Besançon</p>
    <p class="widget-coords">47.3°/6° 265m</p>
    <div class="forecast">
      <div class="day-name">mer.</div><div class="day-name">jeu.</div><div class="day-name">ven.</div><div class="day-name">sam.</div><div class="day-name">dim.</div>
      <div class="day-date">07.08</div><div class="day-date">08.08</div><div class="day-date">09.08</div><div class="day-date">10.08</div><div class="day-date">11.08</div>
      <div class="day-icon" role="img" aria-label="Thunderstorm weather symbol"></div>
      <div class="day-icon" role="img" aria-label="Sun and cloud with showers weather symbol"></div>
      <div class="day-icon" role="img" aria-label="Sun and cloud with showers weather symbol"></div>
      <div class="day-icon" role="img" aria-label="Sun and cloud weather symbol"></div>
      <div class="day-icon" role="img" aria-label="Sun and cloud weather symbol"></div>
      <div class="temp t-amber">24 <small>°C</small></div><div class="temp t-yellow">20 <small>°C</small></div><div class="temp t-amber">24 <small>°C</small></div><div class="temp t-amber">25 <small>°C</small></div><div class="temp t-orange">27 <small>°C</small></div>
      <div class="temp t-lime">16 <small>°C</small></div><div class="temp t-green">15 <small>°C</small></div><div class="temp t-deep">13 <small>°C</small></div><div class="temp t-deep">12 <small>°C</small></div><div class="temp t-deep">12 <small>°C</small></div>
      <div class="wind">35 <small>km/h</small></div><div class="wind">12 <small>km/h</small></div><div class="wind">13 <small>km/h</small></div><div class="wind">14 <small>km/h</small></div><div class="wind">11 <small>km/h</small></div>
    </div>
  </section>

  <div class="brand">skyvela</div>

  <section class="pitch">
    <p class="lead">Add some valuable information to your site with our</p>
    <h1 class="headline">FREE HTML WIDGET</h1>
    <ul class="benefits">
      <li>Absolutely FREE</li>
      <li>Worldwide information</li>
      <li>Easy to integrate</li>
      <li>Multilangual</li>
    </ul>
    <a class="cta" href="http://www.skyvela.example/en_GB/weather/forecast/widgetsetup">
      FIND MORE INFORMATION
      <svg width="17" height="17" viewBox="0 0 17 17" aria-hidden="true">
        <circle cx="8.5" cy="8.5" r="8.5" fill="var(--blue)"/>
        <path d="M4.5 8.5h7M8.5 5l3.5 3.5L8.5 12" fill="none" stroke="#fff" stroke-width="2" stroke-linecap="round" stroke-linejoin="round"/>
      </svg>
    </a>
  </section>
</div>
</body>
</html>
```